Maplecrest Ambulatory Flyer

Need to make a flyer similar to the attached Tri Vale pdfs for Maplecrest Ambulatory. The write up is attached or can be found at https://www.medivantasc.com/bronx

Requirements
Must have
• What the existing flyer has.

```html
<!DOCTYPE html>
<html lang="en">
<head>
<meta charset="utf-8">
<title>Maplecrest Ambulatory Surgery Center Flyer</title>
<link rel="stylesheet" href="https://fonts.googleapis.com/css2?family=Montserrat:wght@400;500;700;800;900&display=swap">
<style>
:root{
  --brand-blue:#2d5fab;
  --brand-cyan:#30c0e3;
  --panel-bg:#f1f3f4;
  --ink:#222b36;
  --white:#ffffff;
  --accent-yellow:#f7ec3b;
  --map-bg:#eceef0;
}
*{box-sizing:border-box;margin:0;padding:0}
html,body{width:1200px;height:764px;overflow:hidden;background:#fff}
body{position:relative;font-family:"Montserrat",sans-serif;color:var(--ink)}
.page{position:absolute;top:58px;width:455px;height:638px;background:var(--panel-bg);overflow:hidden}
.page--front{left:72px}
.page--back{left:684px}
.wave{position:absolute;left:0;top:0;width:455px;height:638px}

/* front */
.masthead{position:absolute;left:0;top:0;width:455px;height:92px;display:flex;align-items:center;justify-content:center;gap:12px;border-bottom:4px solid var(--brand-blue)}
.brand-mark{width:14px;height:14px;background:var(--brand-blue);flex:none}
.brand-name{font-weight:800;font-size:21px;line-height:1.15;color:#111;text-align:center;letter-spacing:.3px;white-space:nowrap}
.welcome{position:absolute;left:34px;top:112px}
.welcome h1{font-weight:900;font-size:26px;line-height:30px;color:var(--brand-blue);letter-spacing:.5px}
.welcome p{font-size:11.4px;line-height:13.5px;width:380px;letter-spacing:.3px}
.info-head{position:absolute;left:0;width:455px;text-align:center;color:var(--white);font-weight:800;font-size:10.2px;line-height:12px;letter-spacing:1.2px;white-space:nowrap}
.info-text{position:absolute;left:30px;width:395px;text-align:center;color:var(--white);font-size:8.2px;line-height:9.7px;letter-spacing:.3px}
.offer-title{position:absolute;left:0;top:482px;width:455px;text-align:center;font-size:25px;font-weight:500;color:var(--brand-blue);letter-spacing:.5px}
.offer-list{position:absolute;top:520px;list-style:none;font-size:14.2px;letter-spacing:1.2px;line-height:17.3px;color:var(--ink)}
.offer-list li::before{content:"• ";font-size:10px;vertical-align:2px}
.offer-list--left{left:40px}
.offer-list--right{left:235px}
.footer-band{position:absolute;left:0;bottom:0;width:455px;height:39px;background:var(--brand-blue);display:flex;align-items:center;justify-content:center;color:var(--accent-yellow);font-weight:900;font-size:16px;letter-spacing:.2px}

/* back */
.photo{position:absolute;left:0;top:0;width:455px;height:270px;background:linear-gradient(180deg,#f4f4f0 0%,#fbfbf8 40%,#e9eef6 75%,#dfe6f1 100%)}
.photo-crowd{position:absolute;left:140px;top:95px;width:180px;height:175px;background:radial-gradient(ellipse at 50% 55%,#7d99c9 0%,#a8bbdd 45%,rgba(233,238,246,0) 75%)}
.priority{position:absolute;left:0;top:42px;width:455px;text-align:center;font-weight:900;font-size:12.6px;line-height:19.5px;color:var(--brand-blue);letter-spacing:.2px}
.cta{position:absolute;left:0;top:270px;width:455px;text-align:center;font-weight:900;font-size:13.2px;line-height:19.5px;color:var(--white);letter-spacing:.2px}
.contact-brand{position:absolute;left:30px;top:352px;width:194px;height:54px;display:flex;align-items:center;justify-content:center;gap:8px;border-bottom:2px solid var(--brand-blue);padding-bottom:4px}
.contact-brand .brand-mark{width:9px;height:9px}
.contact-brand .brand-name{font-size:11px}
.contact-details{position:absolute;left:228px;top:356px;width:215px;text-align:center;font-size:11.2px;line-height:13.4px;letter-spacing:.3px;font-style:normal}
.map{position:absolute;left:0;top:423px;width:455px;height:176px;background:var(--map-bg)}
</style>
</head>
<body>

<section class="page page--front">
  <svg class="wave" viewBox="0 0 455 638" aria-hidden="true">
    <defs>
      <linearGradient id="bandFront" x1="0" x2="1" y1="0" y2="0">
        <stop offset="0" stop-color="#2d5fab"/>
        <stop offset="1" stop-color="#30c0e3"/>
      </linearGradient>
    </defs>
    <path d="M0,165 C0,193 28,202 62,202 L428,202 C445,202 455,216 455,234 L455,510 C442,482 422,471 398,471 L40,471 C14,471 0,452 0,430 Z" fill="url(#bandFront)"/>
  </svg>

  <header class="masthead">
    <span class="brand-mark"></span>
    <div class="brand-name">Maplecrest<br>Ambulatory Surgery Center</div>
  </header>

  <div class="welcome">
    <h1>WELCOME!</h1>
    <p>Maplecrest Ambulatory Surgery Center, is a same day surgical center, conveniently located in the Bronx, licensed by the state of New York and accredited by NAHCA.</p>
  </div>

  <h2 class="info-head" style="top:223px">CONVENIENT LOCATION FOR PATIENTS AND SURGEONS</h2>
  <p class="info-text" style="top:239px">Maplecrest Ambulatory Surgery Center is conveniently located on Larkin Avenue in the Bronx, and is easily accessed from Manhattan, Westchester and Long Island with ample parking available on site.</p>

  <h2 class="info-head" style="top:284px">CAPABILITIES OF MAPLECREST AMBULATORY SURGERY CENTER</h2>
  <p class="info-text" style="top:300px">Maplecrest Ambulatory Surgery Center is a dedicated facility for same day procedures that do not require an overnight hospital stay, without sacrificing the quality of care and safety that a hospital provides. With over 15,000 sq. ft of space and four operating rooms, the center offers specialties including orthopedics, pain management, podiatry, ophthalmology, ENT, pediatric ENT, and general surgery. These same day procedures, are performed by Maplecrest Ambulatory Surgery Center’s highly skilled medical professionals that are committed to patient safety and satisfaction, providing the highest caliber of care with warmth and compassion in a personalized environment.</p>

  <h2 class="info-head" style="top:389px">BENEFITS OF CHOOSING</h2>
  <p class="info-text" style="top:403px">More surgeons are choosing same day surgery centers because of the ability to provide high quality care in a state-of-the-art facility, at a more reasonable cost to you, your insurance provider, and your employer. Perhaps most importantly, same day surgery requires less down time, which means you’ll spend less time away from your family and your job, and in most instances, you can return to your daily routine the next day.</p>

  <h2 class="offer-title">WE OFFER YOU</h2>
  <ul class="offer-list offer-list--left">
    <li>ORTHOPEDICS</li>
    <li>PAIN MANAGEMENT</li>
    <li>PODIATRY</li>
  </ul>
  <ul class="offer-list offer-list--right">
    <li>OPHTHALMOLOGY</li>
    <li>ENT &amp; PEDIATRIC ENT</li>
    <li>GENERAL SURGERY</li>
  </ul>

  <footer class="footer-band">4210 Larkin Ave, Bronx, NY 10467</footer>
</section>

<section class="page page--back">
  <div class="photo" role="img" aria-label="Photo of a surgical team in scrubs and white coats walking down a bright hospital corridor">
    <div class="photo-crowd"></div>
  </div>
  <p class="priority">HERE AT MAPLECREST AMBULATORY SURGERY CENTER,<br>THE PATIENT IS OUR NUMBER ONE PRIORITY.</p>

  <svg class="wave" viewBox="0 0 455 638" aria-hidden="true">
    <defs>
      <linearGradient id="bandBack" x1="0" x2="1" y1="0" y2="0">
        <stop offset="0" stop-color="#2d5fab"/>
        <stop offset="1" stop-color="#30c0e3"/>
      </linearGradient>
    </defs>
    <path d="M0,230 C4,250 20,259 50,259 L428,259 C445,259 455,274 455,292 L455,378 C442,352 422,340 398,340 L40,340 C14,340 0,324 0,305 Z" fill="url(#bandBack)"/>
  </svg>

  <p class="cta">TO OFFER YOUR PATIENTS THE HIGHEST CALIBER<br>CARE FOR SAME-DAY SURGERIES, CONTACT MAPLECREST<br>AMBULATORY SURGERY CENTER TODAY.</p>

  <div class="contact-brand">
    <span class="brand-mark"></span>
    <div class="brand-name">Maplecrest<br>Ambulatory Surgery Center</div>
  </div>

  <address class="contact-details">
    4210 Larkin Ave,<br>
    Bronx, NY 10467<br>
    Phone: (718) 555-0142<br>
    Email: info@medivantasc.com
  </address>

  <div class="map" role="img" aria-label="Street map of the surrounding Bronx neighborhood with a pin marking the surgery center"></div>

  <footer class="footer-band">Licensed by the State of New York</footer>
</section>

</body>
</html>
```